Business Card Design Project

Dunmore Freightwerk is an IT focussed, forward thinking online uniform and inventory management company supplying into large scale Defence, Emergency Services and Government Department contracts.

Our logo is our name, however we have adopted the use of a globe (see attached) within a recent promotional DVD and would like this worked into the design.

We are wanting something sharp and sophisticated.

Requirements
Must have
• Space for QR Code
Website details www.dunmorefreightwerk.example
Nice to have
• 2 sided - name/logo only on rear side.

```html
<!DOCTYPE html>
<html lang="en">
<head>
<meta charset="utf-8">
<title>Dunmore Freightwerk – Business Card</title>
<link rel="stylesheet" href="https://fonts.googleapis.com/css2?family=Arimo:wght@400;700&family=Cinzel:wght@400&family=Open+Sans:wght@400&family=Roboto+Condensed:wght@400&display=swap">
<style>
  :root {
    --ink: #000000;
    --paper: #ffffff;
    --stripe: #8a8a8a;
    --brand-grey: #7a7a7a;
    --mark: #5d636b;
    --label: #1c2b3a;
    --muted-light: #c4c4c4;
    --url-grey: #b8b8b8;
    --qr-line: #6a6a6a;
  }
  html, body {
    margin: 0;
    padding: 0;
    width: 857px;
    height: 1200px;
    overflow: hidden;
    background: var(--paper);
  }
  .sheet {
    position: relative;
    width: 857px;
    height: 1200px;
  }
  .card {
    position: absolute;
    left: 23px;
    width: 812px;
    height: 464px;
    background: var(--ink);
    overflow: hidden;
  }
  .card--front { top: 16px; }
  .card--back { top: 618px; }

  .front-wave {
    position: absolute;
    inset: 0;
    width: 100%;
    height: 100%;
  }
  .brand-dot {
    position: absolute;
    left: 78px;
    top: 66px;
    width: 96px;
    height: 96px;
    border-radius: 50%;
    background: var(--mark);
  }
  .brand-name {
    position: absolute;
    left: 206px;
    top: 100px;
    margin: 0;
    font-family: "Cinzel", serif;
    font-weight: 400;
    font-size: 34px;
    letter-spacing: 2px;
    line-height: 1;
    text-transform: uppercase;
    color: var(--brand-grey);
    white-space: nowrap;
  }
  .holder {
    position: absolute;
    right: 89px;
    top: 198px;
    text-align: right;
    font-family: "Roboto Condensed", sans-serif;
    color: var(--ink);
  }
  .holder__name {
    margin: 0;
    font-size: 42px;
    line-height: 46px;
  }
  .holder__role {
    margin: 0;
    font-size: 23px;
    line-height: 28px;
  }
  .contact {
    position: absolute;
    left: 37px;
    top: 344px;
    margin: 0;
    font-family: "Open Sans", sans-serif;
    font-size: 18px;
    line-height: 23px;
    color: var(--paper);
  }
  .email {
    position: absolute;
    right: 41px;
    top: 408px;
    margin: 0;
    font-family: "Open Sans", sans-serif;
    font-size: 21px;
    color: var(--paper);
  }

  .back-dot {
    position: absolute;
    left: 338px;
    top: 94px;
    width: 104px;
    height: 104px;
    border-radius: 50%;
    background: var(--mark);
  }
  .website {
    position: absolute;
    left: 0;
    right: 0;
    top: 263px;
    margin: 0;
    text-align: center;
    font-family: "Open Sans", sans-serif;
    font-size: 19px;
    letter-spacing: 10px;
    color: var(--url-grey);
    white-space: nowrap;
  }
  .tagline {
    position: absolute;
    left: 0;
    right: 0;
    top: 352px;
    margin: 0;
    text-align: center;
    font-family: "Arimo", sans-serif;
    font-size: 15px;
    line-height: 22px;
    color: var(--muted-light);
  }
  .qr-space {
    position: absolute;
    right: 22px;
    bottom: 20px;
    width: 62px;
    height: 62px;
    box-sizing: border-box;
    border: 1px solid var(--qr-line);
  }

  .side-label {
    position: absolute;
    left: 0;
    right: 0;
    margin: 0;
    text-align: center;
    font-family: "Arimo", sans-serif;
    font-weight: 700;
    font-size: 40px;
    line-height: 1;
    color: var(--label);
  }
  .side-label--front { top: 527px; }
  .side-label--back { top: 1130px; }
</style>
</head>
<body>
<main class="sheet">

  <section class="card card--front" aria-label="Card front">
    <svg class="front-wave" viewBox="0 0 696 398" preserveAspectRatio="none" aria-hidden="true">
      <path d="M0,233 L590,282 L0,254 Z" fill="var(--stripe)"/>
      <path d="M0,0 H696 L679,228 Q668,282 612,282 L0,216 Z" fill="var(--paper)"/>
    </svg>
    <span class="brand-dot" aria-hidden="true"></span>
    <h1 class="brand-name">Dunmore Freightwerk</h1>
    <div class="holder">
      <p class="holder__name">Persons Name</p>
      <p class="holder__role">Implementation Partner</p>
    </div>
    <p class="contact">
      Dunmore Freightwerk Pty Ltd.<br>
      Sydney &amp; Melbourne<br>
      Tel +61 2 9000 0148<br>
      Fax +61 2 9000 0193
    </p>
    <p class="email">mhale@dunmorefreightwerk.example</p>
  </section>

  <h2 class="side-label side-label--front">FRONT</h2>

  <section class="card card--back" aria-label="Card back">
    <span class="back-dot" aria-hidden="true"></span>
    <p class="website">www.dunmorefreightwerk.example</p>
    <p class="tagline">
      IT focussed, forward thinking online uniform &amp; inventory management company supplying<br>
      into large scale Defence, Emergency Services &amp; Government Department contracts.
    </p>
    <span class="qr-space" role="img" aria-label="Space reserved for QR code"></span>
  </section>

  <h2 class="side-label side-label--back">BACK</h2>

</main>
</body>
</html>
```